Wix web design for healthcare IT consulting firm.

I am looking for a web design built in Wix that it will be easy for me to add or edit content in the future. The web site does not need to be overly complicated, but it should look very polished and professional. I also want to ensure it is mobile device friendly. I do not need any type of on-line purchasing ability. I will eventually do blogs, but for now it is a fairly standard web site with main page, about us, services provided, etc. I would also like a place for potential customers to contact us directly from the web site. I have included a Word document with some content for the web design. I have also included my logo and business card for reference. I would like to utilize similar colors as my business card. One of my primary competitors is https://vonmarlhq.example/

Target Market(s)

Target market could be nursing home CEO, CIO, or other leader at an organization that manages long term care facilities.

Number of Pages Required

5+ page

Colors
876aae

Requirements
Must have
• Be designed to be used in Wix. Use the content I provided to create and make web design. Allow to be viewed on mobile device. Please use similar color structure as attached business card. Please use attached logo in design.

```html
<!DOCTYPE html>
<html lang="en">
<head>
<meta charset="utf-8">
<title>Meridell Health Systems</title>
<link href="https://fonts.googleapis.com/css2?family=Roboto:wght@400;500;700&family=Lato:wght@400;700&display=swap" rel="stylesheet">
<style>
:root{
  --purple:#6a4598;
  --purple-deep:#5b3a86;
  --ink:#1f1f1f;
  --text:#444;
  --muted:#777;
  --white:#fff;
  --field:#f2f2f2;
  --footer:#2b2b2b;
}
*{box-sizing:border-box;margin:0;padding:0}
html,body{width:1200px;height:4511px;overflow:hidden}
body{font-family:"Lato",Arial,sans-serif;color:var(--text);background:var(--white);font-size:15px;line-height:1.5}
h1,h2,h3,h4{font-family:"Roboto",Arial,sans-serif;color:var(--ink)}
.section{position:relative;width:1200px}
.abs{position:absolute}

/* header */
.site-header{height:120px}
.menu-icon{left:118px;top:45px}
.brand{left:523px;top:22px;width:154px;text-align:center}
.brand-name{font-family:"Roboto",Arial,sans-serif;font-weight:700;font-size:34px;color:var(--purple);line-height:1}
.header-phone{left:944px;top:44px;display:flex;align-items:center;gap:10px;font-size:15px;color:var(--text)}

/* hero */
.hero{height:675px;background:linear-gradient(135deg,#d6dbe0 0%,#b9c2cb 40%,#c7ced6 70%,#e3e6ea 100%)}
.hero-title{position:absolute;left:0;right:0;top:340px;text-align:center;color:var(--white);font-family:"Roboto",Arial,sans-serif;font-weight:700;font-size:27px;line-height:1.3;text-shadow:0 2px 6px rgba(0,0,0,.45)}

/* about */
.about{height:525px}
.about h2{left:120px;top:110px;font-size:32px;font-weight:700}
.about-copy{left:120px;top:175px;width:460px;font-size:14px;line-height:1.55;color:var(--ink)}
.about-copy p+p{margin-top:16px}
.btn-outline{display:inline-block;border:2px solid var(--ink);color:var(--ink);font-size:14px;padding:11px 40px;background:var(--white)}
.about .btn-outline{left:120px;top:345px}
.about-photo{left:628px;top:102px;width:488px;height:308px;background:linear-gradient(135deg,#2f4f7a,#6f8fb5 50%,#a9bfd6)}

/* services */
.services{height:700px;background:var(--purple)}
.section-title-light{position:absolute;left:0;right:0;text-align:center;color:var(--white);font-family:"Roboto",Arial,sans-serif;font-weight:700;font-size:30px}
.services .section-title-light{top:45px}
.service-card{position:absolute;background:var(--white);text-align:center;padding-top:28px;border-bottom:4px solid #ddd}
.service-card h3{font-size:15px;font-weight:700;margin-top:10px}
.service-card p{font-size:14px;color:var(--text);margin:12px auto 0;width:220px;line-height:1.45}
.read-more{display:inline-flex;align-items:center;gap:6px;font-size:13px;color:var(--text);margin-top:10px}

/* IT services */
.it-services{height:760px}
.it-services h2{position:absolute;left:0;right:0;top:45px;text-align:center;font-size:30px;font-weight:700}
.it-tile{position:absolute;width:292px}
.it-photo{height:224px}
.it-tile h3{text-align:center;font-size:15px;font-weight:700;margin-top:15px}

/* blogs */
.blogs{height:700px;background:var(--purple)}
.blogs .section-title-light{top:65px}
.slider-nav{left:1020px;top:75px;display:flex;gap:12px}
.blog-card{position:absolute;top:135px;width:292px;height:395px;background:var(--white)}
.blog-photo{height:212px}
.blog-link{position:absolute;left:123px;top:188px;width:46px;height:46px;border-radius:50%;background:var(--purple);border:3px solid var(--white);display:flex;align-items:center;justify-content:center}
.blog-head{display:flex;justify-content:space-between;align-items:baseline;padding:0 22px;margin-top:48px}
.blog-head h3{font-size:18px;font-weight:700}
.blog-date{font-size:14px;color:var(--ink)}
.blog-card p{padding:0 22px;font-size:14px;color:var(--ink);margin-top:8px;line-height:1.45}
.blog-meta{display:flex;align-items:center;padding:0 22px;margin-top:20px;font-size:14px;color:var(--ink)}
.blog-meta .stats{margin-left:auto;display:flex;gap:14px;align-items:center}
.blog-meta .stats span{display:inline-flex;align-items:center;gap:5px}
.btn-light{left:528px;top:573px;border:2px solid var(--white);color:var(--white);font-size:14px;padding:11px 38px}

/* contact */
.contact{height:630px}
.contact h2{left:120px;top:100px;font-size:26px;font-weight:700}
.contact-intro{left:130px;top:145px;width:390px;font-size:14px;color:var(--ink);line-height:1.5}
.contact-form{left:120px;top:205px;width:387px}
.field{height:45px;background:var(--field);margin-bottom:14px;padding:12px 14px;font-size:14px;color:var(--muted)}
.field.message{height:110px}
.btn-submit{display:inline-block;background:var(--purple);color:var(--white);font-weight:700;font-size:14px;padding:11px 42px}
.contact .map-title{left:600px;top:100px;font-size:26px;font-weight:700}
.map{left:600px;top:150px;width:480px;height:390px;background:linear-gradient(160deg,#cfe0c2 0%,#e6e2cf 45%,#d9d3bd 70%,#b8d0e3 100%)}

/* footer */
.site-footer{height:330px;background:var(--footer);color:#e5e5e5}
.footer-brand{left:120px;top:70px;font-family:"Roboto",Arial,sans-serif;font-weight:700;font-size:32px;color:var(--white);line-height:1}
.footer-about{left:120px;top:130px;width:200px;font-size:14px;line-height:1.45}
.footer-about .read-more{color:#e5e5e5}
.footer-col{top:70px}
.footer-col h4{color:var(--white);font-size:14px;font-weight:700;letter-spacing:.5px}
.footer-col h4::after{content:"";display:block;width:80px;height:2px;background:var(--white);margin-top:8px}
.quick-links{left:397px}
.quick-links ul{list-style:none;margin-top:14px;font-family:"Roboto",Arial,sans-serif;font-weight:700;font-size:14px;color:var(--white)}
.quick-links li{display:flex;align-items:center;gap:10px;line-height:24.5px}
.office{left:645px}
.office ul{list-style:none;margin-top:14px;font-size:14px}
.office li{display:flex;gap:12px;align-items:flex-start;line-height:24px}
.office svg{flex:none;margin-top:5px}
.subscribe{left:860px}
.subscribe p{font-size:14px;margin-top:14px;width:230px;line-height:1.5}
.subscribe-form{display:flex;margin-top:16px;width:220px}
.subscribe-form .input{flex:1;background:var(--white);color:var(--muted);font-size:12px;padding:7px 10px;height:32px}
.subscribe-form .go{width:32px;height:32px;background:var(--purple);display:flex;align-items:center;justify-content:center}

.copyright-bar{height:71px;background:var(--purple-deep);color:var(--white)}
.copyright-bar p{position:absolute;left:120px;top:24px;font-size:13px}
.social{right:120px;top:20px;display:flex;gap:8px}
.social span{width:30px;height:30px;border-radius:50%;background:var(--white)}
</style>
</head>
<body>

<header class="section site-header">
  <svg class="abs menu-icon" width="22" height="18" viewBox="0 0 22 18"><rect y="0" width="22" height="3" fill="#6a4598"/><rect y="7.5" width="22" height="3" fill="#6a4598"/><rect y="15" width="22" height="3" fill="#6a4598"/></svg>
  <div class="abs brand"><div class="brand-name">Meridell</div></div>
  <div class="abs header-phone">
    <svg width="22" height="22" viewBox="0 0 24 24" fill="none" stroke="#6a4598" stroke-width="2"><circle cx="12" cy="12" r="10.5"/><path d="M8.5 7.5l2 2-1 1.5c.8 1.6 1.9 2.7 3.5 3.5l1.5-1 2 2-1.2 1.3c-3.5-.4-7.2-4.1-7.6-7.6z" fill="#6a4598" stroke="none"/></svg>
    <span>(555) 201 3846</span>
  </div>
</header>

<section class="section hero" role="img" aria-label="Overhead view of a clinician's desk with laptop, stethoscope, keyboard, phone and clipboard">
  <h1 class="hero-title">Increasing The Value and Security<br>of Your Technology Resources</h1>
</section>

<section class="section about">
  <h2 class="abs">About us</h2>
  <div class="abs about-copy">
    <p>Lorem Ipsum is simply dummy text of the printing and typesetting ustry. Lorem Ipsum the industry's standard dummy text ever since the 1500s.</p>
    <p>Lorem Ipsum is simply dummy text of the printing and typesetting ind ustry. Lorem Ipsum has been the industry's standard dummy text ever since the 1500s, when an unknown printer took a galley of type and scrambled it to make a type specimen book.</p>
  </div>
  <a class="abs btn-outline">Read More</a>
  <div class="abs about-photo" role="img" aria-label="Business team reviewing charts on a tablet and paperwork"></div>
</section>

<section class="section services">
  <h2 class="section-title-light">Our Services</h2>

  <div class="service-card" style="left:120px;top:115px;width:291px;height:215px">
    <svg width="40" height="36" viewBox="0 0 40 36" fill="none" stroke="#1f1f1f" stroke-width="2.5"><path d="M3 8h12l4 4h18v20H3z"/><path d="M20 16v12M14 22h12" stroke-width="3"/></svg>
    <h3>Electronic Health Record (EHR)</h3>
    <p>Lorem Ipsum is simply dummy text of the printing and typesetting.</p>
    <span class="read-more">Read More <svg width="12" height="12" viewBox="0 0 12 12"><circle cx="6" cy="6" r="5" fill="none" stroke="#444"/><path d="M5 3.5L7.5 6 5 8.5" fill="none" stroke="#444"/></svg></span>
  </div>
  <div class="service-card" style="left:453px;top:115px;width:291px;height:215px">
    <svg width="40" height="36" viewBox="0 0 40 36" fill="none" stroke="#1f1f1f" stroke-width="2.5"><rect x="3" y="3" width="34" height="24" rx="2"/><path d="M14 33h12M20 27v6"/><circle cx="20" cy="15" r="5"/><path d="M20 7v3M20 20v3M12 15h3M25 15h3"/></svg>
    <h3>EHR Optimization Services</h3>
    <p>Lorem Ipsum is simply dummy text of the printing and typesetting.</p>
    <span class="read-more">Read More <svg width="12" height="12" viewBox="0 0 12 12"><circle cx="6" cy="6" r="5" fill="none" stroke="#444"/><path d="M5 3.5L7.5 6 5 8.5" fill="none" stroke="#444"/></svg></span>
  </div>
  <div class="service-card" style="left:786px;top:115px;width:291px;height:215px">
    <svg width="36" height="40" viewBox="0 0 36 40" fill="none" stroke="#1f1f1f" stroke-width="2.5"><rect x="4" y="6" width="24" height="31" rx="2"/><rect x="11" y="3" width="10" height="6" rx="1" fill="#1f1f1f"/><path d="M9 18h14M9 24h10M9 30h8"/><circle cx="28" cy="30" r="6" fill="#fff"/><path d="M25 30l2 2 4-4"/></svg>
    <h3>EHR Assessment</h3>
    <p>Lorem Ipsum is simply dummy text of the printing and typesetting.</p>
    <span class="read-more">Read More <svg width="12" height="12" viewBox="0 0 12 12"><circle cx="6" cy="6" r="5" fill="none" stroke="#444"/><path d="M5 3.5L7.5 6 5 8.5" fill="none" stroke="#444"/></svg></span>
  </div>
  <div class="service-card" style="left:120px;top:390px;width:456px;height:215px">
    <svg width="36" height="40" viewBox="0 0 36 40" fill="none" stroke="#1f1f1f" stroke-width="2.5"><path d="M18 3l13 5v11c0 8-6 14-13 18C11 33 5 27 5 19V8z"/><path d="M12 20l5 5 8-9"/></svg>
    <h3>EHR Quality Assessment</h3>
    <p>Lorem Ipsum is simply dummy text of the printing and typesetting.</p>
    <span class="read-more">Read More <svg width="12" height="12" viewBox="0 0 12 12"><circle cx="6" cy="6" r="5" fill="none" stroke="#444"/><path d="M5 3.5L7.5 6 5 8.5" fill="none" stroke="#444"/></svg></span>
  </div>
  <div class="service-card" style="left:621px;top:390px;width:456px;height:215px">
    <svg width="40" height="40" viewBox="0 0 40 40" fill="none" stroke="#1f1f1f" stroke-width="2.5"><path d="M7 22v-4a13 13 0 0126 0v4"/><rect x="4" y="20" width="7" height="11" rx="2" fill="#1f1f1f"/><rect x="29" y="20" width="7" height="11" rx="2" fill="#1f1f1f"/><path d="M32 31c0 4-4 6-9 6h-3"/></svg>
    <h3>On-Going EHR Support</h3>
    <p>Lorem Ipsum is simply dummy text of the printing and typesetting.</p>
    <span class="read-more">Read More <svg width="12" height="12" viewBox="0 0 12 12"><circle cx="6" cy="6" r="5" fill="none" stroke="#444"/><path d="M5 3.5L7.5 6 5 8.5" fill="none" stroke="#444"/></svg></span>
  </div>
</section>

<section class="section it-services">
  <h2>Information Technology Services</h2>
  <div class="it-tile" style="left:120px;top:140px"><div class="it-photo" role="img" aria-label="Hand writing the word risk on a dark screen" style="background:linear-gradient(135deg,#0f2f3f,#1d5d75 60%,#2d7d90)"></div><h3>Risk Assessment</h3></div>
  <div class="it-tile" style="left:453px;top:140px"><div class="it-photo" role="img" aria-label="Policy sign held over a desk with documents" style="background:linear-gradient(135deg,#8d7b66,#c9b99e 50%,#6d7f92)"></div><h3>Policy Management and Consulting</h3></div>
  <div class="it-tile" style="left:786px;top:140px"><div class="it-photo" role="img" aria-label="Hand touching a hexagon chief information officer graphic" style="background:linear-gradient(135deg,#eaf1f8,#b9d2ea 50%,#5b8fbf)"></div><h3>Chief Information Officer</h3></div>
  <div class="it-tile" style="left:120px;top:430px"><div class="it-photo" role="img" aria-label="Hand on a glowing security lock interface" style="background:linear-gradient(135deg,#173c5f,#3f86b7 55%,#a9d3ef)"></div><h3>Chief Information Security Officer</h3></div>
  <div class="it-tile" style="left:453px;top:430px"><div class="it-photo" role="img" aria-label="Person reviewing a network technology display" style="background:linear-gradient(135deg,#0e2848,#2f6294 55%,#8fb5d8)"></div><h3>IT Department Evaluation</h3></div>
  <div class="it-tile" style="left:786px;top:430px"><div class="it-photo" role="img" aria-label="Consultants pointing at a tablet during a meeting" style="background:linear-gradient(135deg,#2c3f58,#7f95ad 55%,#d7dfe7)"></div><h3>On-Going CIO or CISO Support</h3></div>
</section>

<section class="section blogs">
  <h2 class="section-title-light">Our Blogs</h2>
  <div class="abs slider-nav">
    <svg width="22" height="22" viewBox="0 0 22 22"><circle cx="11" cy="11" r="10" fill="none" stroke="#fff" stroke-width="1.5"/><path d="M12.5 7L8.5 11l4 4" fill="none" stroke="#fff" stroke-width="2"/></svg>
    <svg width="22" height="22" viewBox="0 0 22 22"><circle cx="11" cy="11" r="11" fill="#fff"/><path d="M9.5 7l4 4-4 4" fill="none" stroke="#6a4598" stroke-width="2"/></svg>
  </div>

  <article class="blog-card" style="left:120px">
    <div class="blog-photo" role="img" aria-label="Colleagues shaking hands over a desk with laptop" style="background:linear-gradient(135deg,#8a7b6c,#c4b7a6 50%,#5e6f7e)"></div>
    <span class="blog-link"><svg width="18" height="18" viewBox="0 0 24 24" fill="none" stroke="#fff" stroke-width="2.5"><path d="M10 14a4 4 0 005.7 0l3.5-3.5a4 4 0 00-5.7-5.7L12 6.3"/><path d="M14 10a4 4 0 00-5.7 0l-3.5 3.5a4 4 0 005.7 5.7L12 17.7"/></svg></span>
    <div class="blog-head"><h3>Blog # 1</h3><span class="blog-date">Oct.31.2018</span></div>
    <p>Lorem Ipsum is simply dummy text of the printing and typesetting industry.</p>
    <div class="blog-meta">Read Full Article<span class="stats"><span><svg width="13" height="12" viewBox="0 0 24 22"><path d="M12 20S2 14 2 7.5A5 5 0 0112 5a5 5 0 0110 2.5C22 14 12 20 12 20z" fill="none" stroke="#444" stroke-width="2"/></svg>35</span><span><svg width="13" height="12" viewBox="0 0 24 22"><path d="M3 3h18v12H9l-5 4v-4H3z" fill="none" stroke="#444" stroke-width="2"/></svg>20</span></span></div>
  </article>
  <article class="blog-card" style="left:453px">
    <div class="blog-photo" role="img" aria-label="Businessman seated in a chair reading on a tablet" style="background:linear-gradient(135deg,#3f4650,#7c838a 50%,#b3aea4)"></div>
    <span class="blog-link"><svg width="18" height="18" viewBox="0 0 24 24" fill="none" stroke="#fff" stroke-width="2.5"><path d="M10 14a4 4 0 005.7 0l3.5-3.5a4 4 0 00-5.7-5.7L12 6.3"/><path d="M14 10a4 4 0 00-5.7 0l-3.5 3.5a4 4 0 005.7 5.7L12 17.7"/></svg></span>
    <div class="blog-head"><h3>Blog # 2</h3><span class="blog-date">Oct.31.2018</span></div>
    <p>Lorem Ipsum is simply dummy text of the printing and typesetting industry.</p>
    <div class="blog-meta">Read Full Article<span class="stats"><span><svg width="13" height="12" viewBox="0 0 24 22"><path d="M12 20S2 14 2 7.5A5 5 0 0112 5a5 5 0 0110 2.5C22 14 12 20 12 20z" fill="none" stroke="#444" stroke-width="2"/></svg>40</span><span><svg width="13" height="12" viewBox="0 0 24 22"><path d="M3 3h18v12H9l-5 4v-4H3z" fill="none" stroke="#444" stroke-width="2"/></svg>23</span></span></div>
  </article>
  <article class="blog-card" style="left:786px">
    <div class="blog-photo" role="img" aria-label="Hands holding a phone above a laptop keyboard" style="background:linear-gradient(135deg,#3a2f48,#8c7a92 50%,#d2c1c6)"></div>
    <span class="blog-link"><svg width="18" height="18" viewBox="0 0 24 24" fill="none" stroke="#fff" stroke-width="2.5"><path d="M10 14a4 4 0 005.7 0l3.5-3.5a4 4 0 00-5.7-5.7L12 6.3"/><path d="M14 10a4 4 0 00-5.7 0l-3.5 3.5a4 4 0 005.7 5.7L12 17.7"/></svg></span>
    <div class="blog-head"><h3>Blog # 3</h3><span class="blog-date">Oct.20.2018</span></div>
    <p>Lorem Ipsum is simply dummy text of the printing and typesetting industry.</p>
    <div class="blog-meta">Read Full Article<span class="stats"><span><svg width="13" height="12" viewBox="0 0 24 22"><path d="M12 20S2 14 2 7.5A5 5 0 0112 5a5 5 0 0110 2.5C22 14 12 20 12 20z" fill="none" stroke="#444" stroke-width="2"/></svg>25</span><span><svg width="13" height="12" viewBox="0 0 24 22"><path d="M3 3h18v12H9l-5 4v-4H3z" fill="none" stroke="#444" stroke-width="2"/></svg>20</span></span></div>
  </article>

  <a class="abs btn-light">Read More</a>
</section>

<section class="section contact">
  <h2 class="abs">Quick Contact</h2>
  <p class="abs contact-intro">Please fill out this quick contact form and someone will be in touch with you shortly</p>
  <div class="abs contact-form">
    <div class="field">Name*</div>
    <div class="field">Phone*</div>
    <div class="field">Email*</div>
    <div class="field message">Message</div>
    <span class="btn-submit">Submit</span>
  </div>
  <h2 class="abs map-title">Map</h2>
  <div class="abs map" role="img" aria-label="Road map of the country with a location marker">
    <svg class="abs" style="left:222px;top:150px" width="36" height="48" viewBox="0 0 36 48"><path d="M18 2C9 2 3 9 3 17c0 12 15 29 15 29s15-17 15-29C33 9 27 2 18 2z" fill="#8a2be2"/><circle cx="18" cy="17" r="6" fill="#fff"/></svg>
  </div>
</section>

<footer class="section site-footer">
  <div class="abs footer-brand">Meridell</div>
  <div class="abs footer-about">
    <p>Lorem Ipsum is simply dummy text of the printing and typese tting industry. Lorem Ipsum has been the industry's standard.</p>
    <span class="read-more" style="margin-top:2px">Read More <svg width="12" height="12" viewBox="0 0 12 12"><circle cx="6" cy="6" r="5" fill="none" stroke="#e5e5e5"/><path d="M5 3.5L7.5 6 5 8.5" fill="none" stroke="#e5e5e5"/></svg></span>
  </div>

  <div class="abs footer-col quick-links">
    <h4>QUICK LINKS</h4>
    <ul>
      <li><svg width="6" height="10" viewBox="0 0 6 10"><path d="M1 1l4 4-4 4" fill="none" stroke="#fff" stroke-width="1.8"/></svg>Home</li>
      <li><svg width="6" height="10" viewBox="0 0 6 10"><path d="M1 1l4 4-4 4" fill="none" stroke="#fff" stroke-width="1.8"/></svg>About us</li>
      <li><svg width="6" height="10" viewBox="0 0 6 10"><path d="M1 1l4 4-4 4" fill="none" stroke="#fff" stroke-width="1.8"/></svg>Our Services</li>
      <li><svg width="6" height="10" viewBox="0 0 6 10"><path d="M1 1l4 4-4 4" fill="none" stroke="#fff" stroke-width="1.8"/></svg>Information Technology</li>
      <li><svg width="6" height="10" viewBox="0 0 6 10"><path d="M1 1l4 4-4 4" fill="none" stroke="#fff" stroke-width="1.8"/></svg>Our Blogs</li>
      <li><svg width="6" height="10" viewBox="0 0 6 10"><path d="M1 1l4 4-4 4" fill="none" stroke="#fff" stroke-width="1.8"/></svg>Contact us</li>
    </ul>
  </div>

  <div class="abs footer-col office">
    <h4>OFFICE</h4>
    <ul>
      <li><svg width="11" height="14" viewBox="0 0 12 16"><path d="M6 0a6 6 0 00-6 6c0 4.5 6 10 6 10s6-5.5 6-10a6 6 0 00-6-6z" fill="#fff"/><circle cx="6" cy="6" r="2.2" fill="#2b2b2b"/></svg><span>48 Larkfield Ave, Suite<br>210, USA<br>Zip Code:00000</span></li>
      <li><svg width="12" height="12" viewBox="0 0 24 24"><path d="M6 2l4 4-2 3c1.5 3 4 5.5 7 7l3-2 4 4-3 3C11 20 4 13 3 5z" fill="#fff"/></svg><span>(555) 201 3847</span></li>
      <li><svg width="13" height="10" viewBox="0 0 26 20"><rect width="26" height="20" rx="2" fill="#fff"/><path d="M1 2l12 9 12-9" fill="none" stroke="#2b2b2b" stroke-width="2"/></svg><span>info@meridell.example</span></li>
      <li><svg width="12" height="12" viewBox="0 0 24 24"><circle cx="12" cy="12" r="11" fill="#fff"/><path d="M12 6v6l4 3" fill="none" stroke="#2b2b2b" stroke-width="2.5"/></svg><span>Mon-Sat 9:00am-6 :00pm</span></li>
    </ul>
  </div>

  <div class="abs footer-col subscribe">
    <h4>SUBSCRIBE</h4>
    <p>Get the latest updates and offer Lorem Ipsum is simply dummy text of the printing.</p>
    <div class="subscribe-form">
      <span class="input">Enter Your Email</span>
      <span class="go"><svg width="16" height="14" viewBox="0 0 24 20"><path d="M1 10L23 1l-5 18-7-6z" fill="#fff"/></svg></span>
    </div>
  </div>
</footer>

<div class="section copyright-bar">
  <p>Copyright © Meridell 2018. All Rights Reserved.</p>
  <div class="abs social" aria-label="Social media links">
    <span></span><span></span><span></span><span></span><span></span>
  </div>
</div>

</body>
</html>
```